Insurance Firm needs Stationary and Corporate Identity

We have a logo (provided) - we need a business card, letterhead, booklet cover, Benefit & Travel card design, and brand guide.
LRC (Larkmoor Relief Cooperative) is a National (Canadian) family-run benefits firm. We've been providing alternative benefit models to small and medium sized businesses for almost 25 years! Our goal is to create long-lasting customer relationships by partnering with our clients to become their dedicated benefits division instead of just selling a product to them.

Benefit & Travel Cards: We provide the benefit card to employees to allow them to pay for drugs at their pharmacy and dental services electronically.
The travel card is for medical emergencies while travelling outside of Canada.

Brand Guide: Once the stationary is complete, the brand guide will allow us to streamline the use of our logo's and fonts for internal and external use. We will expect that this will be a paid project for our design winner after the contest closes and we will negotiate the pricetag for this at that time.

Target Market(s)

Business Owners, Entrepreneurs, HR Professionals

Industry/Entity Type

Insurance Agency

Font styles to use
Sans Serif

Requirements
Must have
• business card, letterhead, health card, travel card, booklet cover (some current samples provided)

```html
<!DOCTYPE html>
<html lang="en">
<head>
<meta charset="utf-8">
<title>Larkmoor Relief Cooperative — Folder Cover</title>
<link href="https://fonts.googleapis.com/css2?family=Tenor+Sans&family=Montserrat:wght@500&display=swap" rel="stylesheet">
<style>
  :root {
    --backdrop: #e9e9ea;
    --cover: #2a2b2b;
    --brand-red: #d3222a;
    --brand-grey: #8e9091;
    --rule-grey: #a4a6a7;
    --url-light: #d9d9d9;
  }
  * { margin: 0; padding: 0; box-sizing: border-box; }
  html, body {
    width: 1200px; height: 800px; overflow: hidden;
    background: var(--backdrop);
  }
  .canvas {
    position: relative; width: 1200px; height: 800px;
    display: flex; align-items: center; justify-content: center;
  }
  .folder-cover {
    position: relative;
    width: 540px; height: 730px;
    background: var(--cover);
    border-radius: 0 18px 18px 0;
    overflow: hidden;
  }
  .cover-pattern {
    position: absolute; inset: 0;
    background: radial-gradient(ellipse at 45% 45%, #313232 0%, var(--cover) 70%);
  }
  .brand-lockup {
    position: absolute; left: 0; right: 0; top: 262px;
    display: flex; flex-direction: column; align-items: center;
  }
  .brand-initials {
    font-family: "Tenor Sans", sans-serif;
    font-size: 108px; line-height: 1;
    letter-spacing: 2px;
    color: var(--brand-grey);
  }
  .brand-name {
    margin-top: 18px;
    font-family: "Tenor Sans", sans-serif;
    font-size: 24px; letter-spacing: 0.5px;
    color: var(--brand-red);
    text-transform: uppercase;
  }
  .brand-descriptor {
    margin-top: 4px;
    display: flex; align-items: center; gap: 6px;
    font-family: "Tenor Sans", sans-serif;
    font-size: 19px; letter-spacing: 0.5px;
    color: var(--rule-grey);
    text-transform: uppercase;
  }
  .brand-descriptor .rule {
    width: 32px; height: 1.5px; background: var(--rule-grey);
  }
  .cover-url {
    position: absolute; left: 0; right: 0; bottom: 26px;
    text-align: center;
    font-family: "Montserrat", sans-serif;
    font-weight: 500; font-size: 13px;
    color: var(--url-light);
  }
  .cover-url .domain { color: var(--brand-red); }
</style>
</head>
<body>
  <main class="canvas">
    <section class="folder-cover">
      <div class="cover-pattern" role="img" aria-label="Faint grey abstract flowing line pattern across the dark cover"></div>
      <div class="brand-lockup">
        <div class="brand-initials">LRC</div>
        <div class="brand-name">Larkmoor Relief</div>
        <div class="brand-descriptor"><span class="rule"></span>Cooperative<span class="rule"></span></div>
      </div>
      <p class="cover-url">www.<span class="domain">larkmoorrelief</span>.com</p>
    </section>
  </main>
</body>
</html>
```